Business card design needed

We are a smash repair business and have been in operation for almost 10 years. We have always had a card with a solid yellow background and black car door as a logo. We don't want to stray too far from this as all of our advertising incorporates same.

We do not wish to have anything comical or too wordy.

Industry/Entity Type

Advertising

Contact Information for Business Card

Rhys & Gemma Tolland
Brookvale Ridge Panel Works
Bays 7-11 Wexford Crescent
Laurieton NSW 2443
02 6571 3820
0428 362 057
office@brookvaleridgepanelworks.com.au

Logo Text

Brookvale Ridge Panel Works

Logo styles of interest
Emblem Logo

```html
<!DOCTYPE html>
<html lang="en">
<head>
<meta charset="utf-8">
<title>Brookvale Ridge Panel Works – Business Card</title>
<link rel="stylesheet" href="https://fonts.googleapis.com/css2?family=Arimo:wght@700&display=swap">
<style>
  :root {
    --surround: #7f7f7f;
    --card-yellow: #ffe900;
    --ink: #231f20;
    --ink-soft: #2e2a2b;
  }
  html, body {
    margin: 0;
    padding: 0;
    width: 1200px;
    height: 693px;
    overflow: hidden;
    background: var(--surround);
  }
  .card {
    position: absolute;
    left: 47px;
    top: 47px;
    width: 1105px;
    height: 598px;
    background: var(--card-yellow);
    color: var(--ink);
    font-family: "Arimo", Helvetica, Arial, sans-serif;
    font-weight: 700;
    overflow: hidden;
  }
  .business-name {
    position: absolute;
    left: 40px;
    top: 38px;
    margin: 0;
    font-size: 57px;
    font-weight: 700;
    line-height: 62px;
    letter-spacing: -0.3px;
  }
  .emblem-area {
    position: absolute;
    left: 575px;
    top: 56px;
    width: 530px;
    height: 410px;
    background: linear-gradient(160deg, var(--ink-soft), var(--ink));
    border-radius: 18px 0 0 0;
  }
  .owners {
    position: absolute;
    left: 578px;
    top: 188px;
    width: 500px;
    margin: 0;
    text-align: center;
    font-size: 37px;
    line-height: 42px;
    color: var(--card-yellow);
  }
  .contact {
    position: absolute;
    left: 39px;
    top: 294px;
    margin: 0;
    font-style: normal;
    font-size: 27px;
    line-height: 40px;
  }
  .contact .line { display: block; }
  .contact .phone,
  .contact .email,
  .contact .mobile { margin-top: 9px; }
</style>
</head>
<body>
  <div class="card">
    <h1 class="business-name">Brookvale Ridge<br>Panel Works</h1>

    <div class="emblem-area" role="img" aria-label="Brand emblem area: the business's black car door mark on yellow"></div>
    <p class="owners">Rhys &amp; Gemma Tolland</p>

    <address class="contact">
      <span class="line">Works Bays 7-11</span>
      <span class="line">Wexford Crescent</span>
      <span class="line">Laurieton NSW 2443</span>
      <span class="line phone">02 6571 3820</span>
      <span class="line email">office@brookvaleridgepanelworks.com.au</span>
      <span class="line mobile">0428 362 057</span>
    </address>
  </div>
</body>
</html>
```